Fantasy Book Cover for 2nd Book in Ongoing Series

I need a full wrap design for the second book in my fantasy series. I've attached the cover for the first book. I'd like the same font and title style (color can be different) but the rest is open to change as long as it's obvious the books are part of the same series.

Title - Tides of Ashfall
Subtitle - A Novel of the Vestomari Lands
Title/Subtitle Font - Ringbearer
Author - Marguerite Calloway
Author/Blurb Font - Gadugi
Trim Size - 5.5 x 8.5
Pages - 410

Blurb -
Things have gone well for Orlane since her brother reclaimed Ombreval and freed their people: Bremon is becoming a stronger king each day, Halvue has found a home in the castle and its gardens, reports keep pouring in about peace within the lands. So why does Orlane feel antsy, as though something is missing?

When the neighboring king invites Orlane and Bremon to Venhol to rekindle relations and celebrate his birthday, Orlane jumps at the chance to travel again—and search for Dov, who’s still tracking Morvan Quell before the former prince can threaten Ombreval’s hard-won peace.

Venhol proves to be a pleasant realm, and Orlane and her friends settle in, until Bremon’s sanity begins to falter, and murder attempts on a Venholan noble shift to include Orlane and her brother.

With limited options, Orlane and her companions join forces with a Surim warrior and the Venholan princess to protect their loved ones. The farther they run for safety, the more the dangers envelope them and Bremon's grip on reality splinters. How can Orlane save her brother from his own mind?

Basics -
The setting for the story is traditional medieval based fantasy world - tunic/jerkin, boots, cloaks, swords, castles, magic, horses, wooden/stone houses, etc.
The first book mainly took place in the forests, hence the trees. The second is during the summer and moves into a capital city for a large portion of the book, then onto a large wooden ship that is taken over by pirates, then onto an isolated island where the characters are hunted by soldiers and battle them as well as a hurricane. So anything pertaining to any of that is acceptable.
The main storyline is about Orlane trying to help her brother, who's targeted for assassination and battling insanity, which is the result of a voodoo style magic be done on him by a rival, though the characters don't learn that until close to the end. Until then, he thinks he's being haunted by a malevolent person from his past.

I'm open to ideas both with and without the main character on the cover. If you have a design that includes the character, I would like either different images of the same woman, or a woman who at least looks a lot like her, or the picture done in a way that obscures or hides her features enough that you can't tell it's not the same woman. I don't want to use the same image as the first book cover though.

I've finally tracked down more images of the woman on book one, but note, in the one picture she has elf ears and my character is not an elf, so that would need changed. Hopefully this link works.
https://pixlink.io/82hQwTu

Target Market(s)

Adult fantasy readers, I have a roughly 60/40 split on female/male readership

Font styles to use
Other font styles liked:
• Ringbearer for title/subtitle, Gadugi for author/blurb

Requirements
Must have
• Ringbearer font for title and subtitle
Gadugi font for author and blurb
Traditional fantasy world feel - similar to Middle Earth or Westeros in buildings, clothing, traveling, etc.
Nice to have
• sense of adventure
since the last book had a relatively dark cover, I'd like this one a little lighter (but not bright)
Should not have
• While I have a lot of sexual tension in the books, I don't want scantily clad women on the cover. My strong female lead wears a full set of clothes.

```html
<!DOCTYPE html>
<html lang="en">
<head>
<meta charset="utf-8">
<title>Tides of Ashfall – Full Wrap Cover</title>
<link rel="stylesheet" href="https://fonts.googleapis.com/css2?family=Cinzel+Decorative:wght@700;900&family=Open+Sans:wght@400&family=Arimo:wght@400&display=swap">
<style>
  :root {
    --page-grey: #d2d3d5;
    --night: #120d08;
    --night-warm: #2a1c0e;
    --gold-light: #ffe27a;
    --gold-mid: #f6b22a;
    --gold-deep: #d85a10;
    --parchment-light: #e6b94a;
    --parchment-dark: #8a5d1c;
    --ink: #111;
    --white: #ffffff;
  }
  * { margin: 0; padding: 0; box-sizing: border-box; }
  html, body { width: 1200px; height: 1200px; overflow: hidden; background: var(--page-grey); }
  .canvas { position: relative; width: 1200px; height: 1200px; }

  .wrap {
    position: absolute; left: 47px; top: 217px; width: 1106px; height: 765px;
    background:
      radial-gradient(ellipse at 70% 10%, #3a3026 0%, transparent 45%),
      linear-gradient(180deg, var(--night) 0%, #1a120a 60%, var(--night-warm) 100%);
    box-shadow: 8px 8px 10px rgba(0,0,0,.55);
    overflow: hidden;
  }
  .city-scene {
    position: absolute; left: 0; bottom: 0; width: 100%; height: 300px;
    background:
      radial-gradient(ellipse at 12% 90%, rgba(200,110,40,.55), transparent 40%),
      radial-gradient(ellipse at 88% 55%, rgba(40,70,50,.5), transparent 35%),
      linear-gradient(180deg, transparent 0%, rgba(70,45,20,.6) 55%, rgba(110,55,20,.8) 100%);
  }

  .gold-title {
    font-family: "Cinzel Decorative", serif; font-weight: 900;
    background: linear-gradient(180deg, var(--gold-light) 0%, var(--gold-mid) 50%, var(--gold-deep) 100%);
    -webkit-background-clip: text; background-clip: text; color: transparent;
    filter: drop-shadow(2px 3px 0 #5a2a08) drop-shadow(0 0 6px rgba(255,160,40,.35));
    text-align: center; line-height: 1;
  }

  /* Back cover */
  .back-title { position: absolute; left: 150px; top: 68px; width: 310px; }
  .back-title .line-main { display: block; font-size: 46px; }
  .back-title .line-of { display: block; font-size: 34px; margin: 2px 0; }

  .blurb-panel {
    position: absolute; left: 12px; top: 211px; width: 468px; height: 370px;
    background: linear-gradient(160deg, var(--parchment-dark) 0%, var(--parchment-light) 45%, #c98d2a 80%, var(--parchment-dark) 100%);
    clip-path: polygon(0 6%, 8% 0, 30% 5%, 60% 9%, 100% 8%, 100% 96%, 45% 98%, 20% 100%, 0 98%);
    opacity: .92;
  }
  .blurb {
    position: absolute; left: 26px; top: 258px; width: 439px;
    font-family: "Arimo", Arial, sans-serif; font-size: 12px; line-height: 15.5px;
    color: var(--ink); text-align: justify;
  }
  .blurb p + p { margin-top: 15.5px; }

  /* Spine */
  .spine-title {
    position: absolute; left: 532px; top: 58px; height: 390px;
    writing-mode: vertical-rl; font-size: 34px; white-space: nowrap;
  }
  .spine-author {
    position: absolute; left: 543px; top: 531px;
    writing-mode: vertical-rl; font-family: "Open Sans", sans-serif;
    font-size: 21px; color: var(--white); white-space: nowrap;
  }

  /* Front cover */
  .front-title { position: absolute; left: 610px; top: 78px; width: 480px; }
  .front-title .line-main { display: block; font-size: 78px; }
  .front-title .line-of { display: block; font-size: 62px; margin: 4px 0; }
  .subtitle {
    position: absolute; left: 650px; top: 400px; width: 440px; text-align: center;
    font-family: "Cinzel Decorative", serif; font-weight: 700; font-size: 20px;
    color: #f0b860; text-shadow: 1px 1px 0 #4a2508;
  }
  .front-author {
    position: absolute; left: 700px; top: 720px; width: 360px; text-align: center;
    font-family: "Open Sans", sans-serif; font-size: 33px; color: var(--white);
  }
</style>
</head>
<body>
<div class="canvas">
  <section class="wrap">
    <div class="city-scene" role="img" aria-label="Night view of a lantern-lit capital city with domed palaces and arched bridges under a starry sky"></div>

    <div class="back-cover">
      <h2 class="back-title gold-title">
        <span class="line-main">Tides</span><span class="line-of">Of</span><span class="line-main">Ashfall</span>
      </h2>
      <div class="blurb-panel" role="img" aria-label="Torn golden parchment backing the blurb"></div>
      <div class="blurb">
        <p>Things have gone well for Orlane since her brother reclaimed Ombreval and freed their people: Bremon is becoming a stronger king each day, Halvue has found a home in the castle and its gardens, reports keep pouring in about peace within the lands. So why does Orlane feel antsy, as though something is missing?</p>
        <p>When the neighboring king invites Orlane and Bremon to Venhol to rekindle relations and celebrate his birthday, Orlane jumps at the chance to travel again—and search for Dov, who’s still tracking Morvan Quell before the former prince can threaten Ombreval’s hard-won peace.</p>
        <p>Venhol proves to be a pleasant realm, and Orlane and her friends settle in, until Bremon’s sanity begins to falter, and murder attempts on a Venholan noble shift to include Orlane and her brother.</p>
        <p>With limited options, Orlane and her companions join forces with a Surim warrior and the Venholan princess to protect their loved ones. The farther they run for safety, the more the dangers envelope them and Bremon's grip on reality splinters. How can Orlane save her brother from his own mind?</p>
      </div>
    </div>

    <div class="spine">
      <div class="spine-title gold-title">Tides Of Ashfall</div>
      <div class="spine-author">Marguerite Calloway</div>
    </div>

    <div class="front-cover">
      <h1 class="front-title gold-title">
        <span class="line-main">Tides</span><span class="line-of">Of</span><span class="line-main">Ashfall</span>
      </h1>
      <p class="subtitle">A Novel Of The Vestomari Lands</p>
      <p class="front-author">Marguerite Calloway</p>
    </div>
  </section>
</div>
</body>
</html>
```